Brackwell Removals

We are a domestic removals company, providing the following service:
- removals service
- packing service
- packing materials
- storage facility
- furniture dismantling and reassembling
We would like to start a flyer campaign to customers that just agreed for the house sale.
Our strong key points:
- Good Reviews (Ratewharf, Quillon, trulyshifting.com and mingleboard)
- Two Men Service (we do all the heavy work for the customer, and place the furniture and boxes to each room of destination)
- Fully Insured
- We can take bookings 7-days of week
- Free and no-obligation survey (we need to do a house visit first in order to provide a fixed and accurate quote)
- Free Quote
Technical Specs:
Landline number: 01632 960418
Contact email: office@brackwellremovals.example
Address: Unit 14, Larkspire Lane, Northampton NN9 4TX
Website: brackwellremovals.example
Took a look on the onto previous projects on PV.example, and liked several flyers already done by you guys, for this industry
We'd like to integrate the colours from our logo in the flyer as well !!

```html
<!DOCTYPE html>
<html lang="en">
<head>
<meta charset="utf-8">
<title>Brackwell Removals – Flyer</title>
<link href="https://fonts.googleapis.com/css2?family=Lato:wght@400;700;900&family=Roboto+Condensed:wght@700&display=swap" rel="stylesheet">
<style>
:root{
  --teal:#1c8092;
  --orange:#f7941d;
  --dark:#333133;
  --ink:#2b2b2b;
  --light:#e4eff2;
  --white:#ffffff;
  --backdrop:#666666;
}
*{box-sizing:border-box;margin:0;padding:0}
html,body{width:1200px;height:1200px;overflow:hidden}
body{background:var(--backdrop);font-family:"Lato",sans-serif;color:var(--ink);position:relative}
.page{position:absolute;top:201px;width:529px;height:754px;background:var(--white);overflow:hidden}
.page--front{left:41px}
.page--back{left:624px}
.abs{position:absolute}

/* front */
.brand{left:31px;top:34px;display:flex;align-items:center;gap:10px}
.brand__mark{width:64px;height:64px;border-radius:50%;background:var(--teal)}
.brand__name{font-weight:900;font-size:19px;color:var(--teal);line-height:1.05;text-transform:uppercase}
.headline{right:32px;top:38px;text-align:right;font-family:"Roboto Condensed",sans-serif;font-weight:700;font-size:34px;line-height:32px;text-transform:uppercase}
.headline span{display:block}
.headline .teal{color:var(--teal)}
.headline .black{color:#111}
.hero{left:0;top:120px;width:529px;height:346px;background:linear-gradient(180deg,#dfe6ee 0%,#c8cfd8 45%,#c99a66 80%,#b4774a 100%)}
.about{left:0;top:466px;width:529px;height:89px;background:var(--dark);color:var(--white)}
.section-title{font-weight:700;font-size:14px;color:var(--orange);text-transform:uppercase;position:relative;padding-bottom:4px}
.section-title::after{content:"";position:absolute;left:0;bottom:0;width:28px;height:2px;background:var(--orange)}
.about__title{left:31px;top:14px}
.about__lead{left:31px;top:42px;width:150px;font-size:10.5px;line-height:12.5px}
.about__body{left:222px;top:14px;width:277px;font-size:10.3px;line-height:12.5px;text-align:justify}
.services{left:0;top:571px;width:529px;height:120px}
.service{position:absolute;top:0;width:100px;text-align:center;font-size:10.5px;line-height:12.5px}
.service--narrow{width:90px}
.service svg{display:block;margin:0 auto 6px}
.footer{left:0;top:704px;width:529px;height:50px;background:var(--teal);color:var(--white)}
.footer__bar{position:absolute;left:38px;bottom:0;width:453px;height:6px;background:var(--orange)}
.contacts{position:absolute;left:38px;top:13px;display:flex;gap:13px;font-size:10.5px;align-items:center;white-space:nowrap}
.contact{display:flex;align-items:center;gap:6px;white-space:nowrap}
.contact__dot{flex:none;width:19px;height:19px;border-radius:50%;background:var(--orange);display:flex;align-items:center;justify-content:center}

/* back */
.badge{left:34px;top:37px;display:flex;align-items:center;gap:6px}
.badge__shape{width:30px;height:22px;background:var(--orange);border-radius:4px}
.badge__text{font-size:6.5px;color:#777;line-height:9px;text-transform:uppercase}
.badge__text b{font-size:8.5px;color:var(--dark)}
.intro{left:31px;top:76px;width:359px;font-size:10.3px;line-height:12.5px;text-align:justify}
.corner-brand{left:420px;top:38px;width:84px;text-align:center}
.corner-brand__mark{width:40px;height:40px;background:var(--teal);margin:0 auto 6px}
.corner-brand__name{font-weight:900;font-size:12px;line-height:13px;color:var(--teal);text-transform:uppercase}
.story{left:0;top:144px;width:246px;height:256px;background:linear-gradient(90deg,#3a3839,#2e2d2e);color:var(--white)}
.story__block{position:absolute;left:31px;width:199px}
.story p{margin-top:10px;font-size:10.3px;line-height:12.5px;text-align:justify}
.crew-photo{left:246px;top:144px;width:283px;height:256px;background:linear-gradient(160deg,#eef0f2 0%,#c9d0d6 45%,#8fa6b6 70%,#2f5fa8 100%)}
.features{left:0;top:400px;width:529px;height:304px;background:var(--light)}
.feature{position:absolute;width:225px;height:83px;background:var(--white);display:flex;align-items:center;gap:14px;padding-left:16px;padding-right:8px;font-size:10px;line-height:12.5px}
.feature svg{flex:none}
.feature b{text-transform:uppercase;font-weight:700}
.address{position:absolute;left:0;top:16px;width:100%;text-align:center;font-size:10.5px;display:flex;justify-content:center;align-items:center;gap:6px}
</style>
</head>
<body>

<section class="page page--front">
  <div class="abs brand">
    <div class="brand__mark"></div>
    <div class="brand__name">Brackwell<br>Removals</div>
  </div>
  <h1 class="abs headline"><span class="teal">Nationwide &amp;</span><span class="black">Local Removals</span></h1>
  <div class="abs hero" role="img" aria-label="Bright living room with a grey sofa, packed cardboard boxes, a guitar and a potted plant on a parquet floor"></div>

  <div class="abs about">
    <h2 class="abs section-title about__title">About Us</h2>
    <p class="abs about__lead">We are specialised in making your move run as smoothly as possible.</p>
    <p class="abs about__body">We offer satisfaction guaranteed and our proven track record reflect our high standards. While doing so, our aim is always to save you money without and hidden charges at the end, whilst offering a fast and reliable service you can trust, no matter how pressed for time you are.</p>
  </div>

  <div class="abs services">
    <div class="service" style="left:16px">
      <svg width="74" height="74" viewBox="0 0 74 74"><circle cx="37" cy="37" r="35" fill="none" stroke="#aaa" stroke-width="1.5" stroke-dasharray="1.5 2.5"/><path d="M6 37a31 31 0 0 1 62 0" fill="none" stroke="#333133" stroke-width="5"/><circle cx="37" cy="37" r="26" fill="#f7941d"/><g fill="none" stroke="#fff" stroke-width="1.6"><rect x="22" y="28" width="20" height="14"/><path d="M42 32h6l4 5v5h-10z"/><circle cx="28" cy="44" r="2.5"/><circle cx="46" cy="44" r="2.5"/></g></svg>
      Removals Service</div>
    <div class="service" style="left:112px">
      <svg width="74" height="74" viewBox="0 0 74 74"><circle cx="37" cy="37" r="35" fill="none" stroke="#aaa" stroke-width="1.5" stroke-dasharray="1.5 2.5"/><path d="M6 37a31 31 0 0 0 62 0" fill="none" stroke="#333133" stroke-width="5"/><circle cx="37" cy="37" r="26" fill="#f7941d"/><g fill="none" stroke="#fff" stroke-width="1.6"><rect x="25" y="32" width="24" height="16"/><path d="M25 32l-4-6h16l4 6M49 32l4-6H37"/><path d="M33 38v6M41 38v6"/></g></svg>
      Packing Service</div>
    <div class="service" style="left:212px">
      <svg width="74" height="74" viewBox="0 0 74 74"><circle cx="37" cy="37" r="35" fill="none" stroke="#aaa" stroke-width="1.5" stroke-dasharray="1.5 2.5"/><path d="M6 37a31 31 0 0 1 62 0" fill="none" stroke="#333133" stroke-width="5"/><circle cx="37" cy="37" r="26" fill="#f7941d"/><g fill="none" stroke="#fff" stroke-width="1.6"><path d="M28 30l10-4 10 10-12 12-10-10z"/><circle cx="34" cy="32" r="2"/></g></svg>
      Packing Materials</div>
    <div class="service" style="left:312px">
      <svg width="74" height="74" viewBox="0 0 74 74"><circle cx="37" cy="37" r="35" fill="none" stroke="#aaa" stroke-width="1.5" stroke-dasharray="1.5 2.5"/><path d="M6 37a31 31 0 0 0 62 0" fill="none" stroke="#333133" stroke-width="5"/><circle cx="37" cy="37" r="26" fill="#f7941d"/><g fill="none" stroke="#fff" stroke-width="1.6"><rect x="24" y="36" width="12" height="12"/><rect x="38" y="36" width="12" height="12"/><rect x="31" y="24" width="12" height="12"/></g></svg>
      Storage Facility</div>
    <div class="service service--narrow" style="left:415px">
      <svg width="74" height="74" viewBox="0 0 74 74"><circle cx="37" cy="37" r="35" fill="none" stroke="#aaa" stroke-width="1.5" stroke-dasharray="1.5 2.5"/><path d="M6 37a31 31 0 0 1 62 0" fill="none" stroke="#333133" stroke-width="5"/><circle cx="37" cy="37" r="26" fill="#f7941d"/><g fill="none" stroke="#fff" stroke-width="1.6"><path d="M24 26v22M32 26v22M24 34h8M24 40h8"/><path d="M40 26v22M50 26v22M40 36h10"/></g></svg>
      Furniture<br>Dismantling and<br>Reassembling</div>
  </div>

  <footer class="abs footer">
    <div class="contacts">
      <span class="contact"><span class="contact__dot"><svg width="11" height="11" viewBox="0 0 24 24"><path fill="#fff" d="M6.6 10.8a15 15 0 0 0 6.6 6.6l2.2-2.2a1 1 0 0 1 1-.25 11 11 0 0 0 3.6.6 1 1 0 0 1 1 1V20a1 1 0 0 1-1 1A17 17 0 0 1 3 4a1 1 0 0 1 1-1h3.5a1 1 0 0 1 1 1 11 11 0 0 0 .6 3.6 1 1 0 0 1-.25 1z"/></svg></span>01632 960418</span>
      <span class="contact"><span class="contact__dot"><svg width="11" height="11" viewBox="0 0 24 24"><rect x="3" y="6" width="18" height="12" fill="none" stroke="#fff" stroke-width="2"/><path d="M3 6l9 7 9-7" fill="none" stroke="#fff" stroke-width="2"/></svg></span>office@brackwellremovals.example</span>
      <span class="contact"><span class="contact__dot"><svg width="11" height="11" viewBox="0 0 24 24"><g fill="none" stroke="#fff" stroke-width="2"><circle cx="12" cy="12" r="9"/><path d="M3 12h18M12 3c3 3 3 15 0 18M12 3c-3 3-3 15 0 18"/></g></svg></span>brackwellremovals.example</span>
    </div>
    <div class="footer__bar"></div>
  </footer>
</section>

<section class="page page--back">
  <div class="abs badge">
    <div class="badge__shape"></div>
    <div class="badge__text">Certified member<br><b>Trusted Movers</b></div>
  </div>
  <p class="abs intro">We offer satisfaction guaranteed and our proven track record reflect our high standards. While doing so, our aim is always to save you money without and hidden charges at the end, whilst offering a fast and reliable service you can trust, no matter how pressed for time you are.</p>
  <div class="abs corner-brand">
    <div class="corner-brand__mark"></div>
    <div class="corner-brand__name">Brackwell<br>Removals</div>
  </div>

  <div class="abs story">
    <div class="story__block" style="top:26px">
      <h2 class="section-title">Our Mission</h2>
      <p>We know and appreciate just how time consuming and stressful moving can be so our fully insured movers are here to take the hard work out of moving, meaning all you need to worry about is settling into your new property.</p>
    </div>
    <div class="story__block" style="top:152px">
      <h2 class="section-title">How We Do It</h2>
      <p>It doesn't matter how small or large your move is, we're available 7 days a week, even at short notice; we'll provide the boxes, organise your items and offer support every step of the way.</p>
    </div>
  </div>
  <div class="abs crew-photo" role="img" aria-label="Two movers in blue uniforms carrying a white sofa up a staircase"></div>

  <div class="abs features">
    <div class="feature" style="left:30px;top:16px">
      <svg width="42" height="42" viewBox="0 0 42 42"><path d="M4 6h34v22H18l-8 8v-8H4z" fill="none" stroke="#f7941d" stroke-width="2"/><g fill="#f7941d"><path d="M13 13l1.2 2.6 2.8.3-2.1 1.9.6 2.8-2.5-1.4-2.5 1.4.6-2.8-2.1-1.9 2.8-.3z"/><path d="M21 13l1.2 2.6 2.8.3-2.1 1.9.6 2.8-2.5-1.4-2.5 1.4.6-2.8-2.1-1.9 2.8-.3z"/><path d="M29 13l1.2 2.6 2.8.3-2.1 1.9.6 2.8-2.5-1.4-2.5 1.4.6-2.8-2.1-1.9 2.8-.3z"/></g></svg>
      <div><b>Good Reviews</b><br>(Ratewharf, Quillon, trulyshifting.com and mingleboard)</div>
    </div>
    <div class="feature" style="left:274px;top:16px">
      <svg width="42" height="42" viewBox="0 0 42 42"><g fill="none" stroke="#f7941d" stroke-width="2"><rect x="8" y="14" width="26" height="20"/><path d="M8 14l5-7h16l5 7M21 7v27"/></g></svg>
      <div><b>Two Men Service</b><br>(we do all the heavy work for the customer, and place the furniture and boxes to each room of destination)</div>
    </div>
    <div class="feature" style="left:30px;top:112px">
      <svg width="42" height="42" viewBox="0 0 42 42"><g fill="none" stroke="#f7941d" stroke-width="2"><rect x="8" y="5" width="24" height="32" rx="2"/><path d="M20 12l8 3v6c0 6-4 9-8 10-4-1-8-4-8-10v-6z"/></g></svg>
      <div><b>Fully Insured</b></div>
    </div>
    <div class="feature" style="left:274px;top:112px">
      <svg width="42" height="42" viewBox="0 0 42 42"><g fill="none" stroke="#f7941d" stroke-width="2"><rect x="4" y="14" width="22" height="16"/><path d="M26 19h7l5 6v5H26z"/><circle cx="11" cy="32" r="3"/><circle cx="31" cy="32" r="3"/><circle cx="12" cy="10" r="6"/><path d="M9 10l2 2 4-4"/></g></svg>
      <div><b>We can take bookings<br>7-days of week</b></div>
    </div>
    <div class="feature" style="left:30px;top:208px">
      <svg width="42" height="42" viewBox="0 0 42 42"><g fill="none" stroke="#f7941d" stroke-width="2.2"><rect x="8" y="6" width="26" height="32" rx="2"/><path d="M16 4h10v5H16z"/><path d="M14 17l4 4 8-8M14 27h14M14 32h14"/></g></svg>
      <div><b>Free and no-obligation survey</b> (we need to do a house visit first in order to provide a fixed and accurate quote)</div>
    </div>
    <div class="feature" style="left:274px;top:208px">
      <svg width="42" height="42" viewBox="0 0 42 42"><g fill="none" stroke="#f7941d" stroke-width="2"><rect x="6" y="5" width="26" height="32"/><path d="M11 12h12M11 17h12M11 22h8M11 27h8"/></g><rect x="22" y="18" width="16" height="16" fill="#f7941d"/><text x="30" y="31" text-anchor="middle" font-family="Lato,sans-serif" font-weight="700" font-size="13" fill="#fff">$</text></svg>
      <div><b>Free Quote</b></div>
    </div>
  </div>

  <footer class="abs footer">
    <div class="address">
      <svg width="12" height="14" viewBox="0 0 24 28"><path d="M12 26s9-9 9-15a9 9 0 0 0-18 0c0 6 9 15 9 15z" fill="none" stroke="#f7941d" stroke-width="2.5"/><circle cx="12" cy="11" r="3" fill="#f7941d"/></svg>
      Unit 14, Larkspire Lane, Northampton NN9 4TX
    </div>
    <div class="footer__bar"></div>
  </footer>
</section>

</body>
</html>
```